Award-winnning Estate Agent needs a premium version of their 'For Sale' board design

We need a premium option for our 'For Sale' board design. We have a standard board that is attached to this brief, but were are looking to have a premium design version that we will use when selling exclusive properties. Our company name is Harbour Lane Estates and the name for this is exclusive selection is: 'The Harbour Collection'. The design needs to work with our current brand, but have a distinctive PREMIUM feel to it. I have uploaded the barnd guidelines and also some of the exisisting logo variations. We do NOT need a new logo but feel free to play around with colours, fonts, sizes etc. for the sign.

Target Market(s)

Property buyers & house hunters

Industry/Entity Type

Real Estate - Residential Property

Font styles to use
Sans Serif

Requirements
Must have
• A premium fee, must be square design, must be easy to read when driving past the sign
Nice to have
• I'm open ot ideas

```html
<!DOCTYPE html>
<html lang="en">
<head>
<meta charset="utf-8">
<title>Harbour Lane Estates – Premium For Sale Board</title>
<link rel="stylesheet" href="https://fonts.googleapis.com/css2?family=Inter:wght@200;300;400;700;800&display=swap">
<style>
  :root {
    --navy: #112442;
    --navy-soft: #1e3459;
    --gold: #c79a5c;
    --gold-mark: #d4994f;
    --gold-band: #a67c44;
    --white: #ffffff;
    --backdrop: #f1f1f1;
    --swatch-navy: #031d4f;
    --swatch-gold: #ad8439;
    --ink: #1a1a1a;
  }
  * { margin: 0; padding: 0; box-sizing: border-box; }
  html, body { width: 1200px; height: 1200px; overflow: hidden; background: var(--white); }
  body { position: relative; font-family: "Inter", Arial, sans-serif; }

  .backdrop { position: absolute; left: 40px; top: 40px; width: 1120px; height: 892px; background: var(--backdrop); }

  .board {
    position: absolute; left: 236px; top: 122px; width: 741px; height: 727px;
    background: var(--white);
    box-shadow: 2px 4px 8px rgba(0,0,0,0.28);
  }
  .brand-panel {
    position: absolute; left: 26px; top: 21px; width: 688px; height: 411px;
    background: var(--navy); overflow: hidden;
  }
  .flourish-side {
    position: absolute; top: 0; width: 110px; height: 240px;
  }
  .flourish-side.left {
    left: 0;
    background: radial-gradient(ellipse 100% 55% at 0% 50%, var(--navy-soft) 0%, rgba(30,52,89,0.55) 55%, rgba(17,36,66,0) 100%);
  }
  .flourish-side.right {
    right: 0;
    background: radial-gradient(ellipse 100% 55% at 100% 50%, var(--navy-soft) 0%, rgba(30,52,89,0.55) 55%, rgba(17,36,66,0) 100%);
  }

  .brand-mark {
    position: absolute; left: 284px; top: 60px; width: 120px; height: 120px;
    background: var(--gold-mark);
  }

  .brand-name {
    position: absolute; left: 0; width: 100%; top: 222px;
    text-align: center; color: var(--gold);
    font-weight: 700; font-size: 48px; letter-spacing: 0.3px; line-height: 1;
  }
  .crest {
    position: absolute; left: 316px; top: 296px; width: 56px; height: 22px;
    background: radial-gradient(ellipse 50% 60% at 50% 70%, rgba(199,154,92,0.55), rgba(199,154,92,0) 100%);
  }
  .tagline-rules { position: absolute; left: 148px; top: 323px; width: 392px; height: 64px; }
  .tagline {
    position: absolute; left: 0; width: 100%; top: 340px;
    text-align: center; color: var(--gold);
    font-weight: 200; font-size: 30px; letter-spacing: -0.8px; line-height: 1;
    text-transform: uppercase;
  }

  .sale-band {
    position: absolute; left: 26px; top: 446px; width: 688px; height: 125px;
    background: var(--gold-band);
    display: flex; align-items: center; justify-content: center;
  }
  .sale-band span {
    color: var(--white); font-weight: 800; font-size: 112px; letter-spacing: 1px; line-height: 1;
    margin-top: 4px;
  }
  .phone {
    position: absolute; left: 0; width: 100%; top: 590px;
    text-align: center; color: var(--navy);
    font-weight: 700; font-size: 60px; letter-spacing: -1px; line-height: 1;
  }
  .website {
    position: absolute; left: 0; width: 100%; top: 659px;
    text-align: center; color: var(--navy);
    font-weight: 300; font-size: 39px; letter-spacing: -0.5px; line-height: 1;
  }

  .palette-title {
    position: absolute; right: 52px; top: 993px;
    font-weight: 400; font-size: 19px; color: var(--ink); letter-spacing: 0.3px;
  }
  .swatch {
    position: absolute; top: 1052px; width: 92px; height: 92px; border-radius: 50%;
    border: 1px solid #333;
  }
  .swatch.navy { left: 807px; background: var(--swatch-navy); }
  .swatch.gold { left: 931px; background: var(--swatch-gold); }
  .swatch.white { left: 1056px; background: var(--white); }
</style>
</head>
<body>
  <div class="backdrop"></div>

  <div class="board">
    <div class="brand-panel">
      <div class="flourish-side left" role="img" aria-label="Faint navy scroll ornament"></div>
      <div class="flourish-side right" role="img" aria-label="Faint navy scroll ornament"></div>

      <div class="brand-mark" aria-hidden="true"></div>
      <div class="brand-name">Harbour Lane Estates</div>

      <div class="crest" role="img" aria-label="Small gold scroll ornament"></div>

      <svg class="tagline-rules" viewBox="0 0 392 64" aria-hidden="true">
        <line x1="10" y1="3" x2="382" y2="3" stroke="#c79a5c" stroke-width="1"/>
        <line x1="10" y1="61" x2="382" y2="61" stroke="#c79a5c" stroke-width="1"/>
        <circle cx="4" cy="3" r="2" fill="#c79a5c"/>
        <circle cx="388" cy="3" r="2" fill="#c79a5c"/>
        <circle cx="4" cy="61" r="2" fill="#c79a5c"/>
        <circle cx="388" cy="61" r="2" fill="#c79a5c"/>
      </svg>
      <div class="tagline">The Harbour Collection</div>
    </div>

    <div class="sale-band"><span>FOR SALE</span></div>

    <div class="phone">01632 960418</div>
    <div class="website">www.harbourlaneestates.co.uk</div>
  </div>

  <div class="palette-title">COLOUR PALETTE</div>
  <div class="swatch navy"></div>
  <div class="swatch gold"></div>
  <div class="swatch white"></div>
</body>
</html>
```